Art for parenting podcast with straight/direct talk...no fluff here! "Plain Answers for Families"

I need an image that will not look fluffy or soft. A no-nonsense look. This is not a 'I love parenting' podcast. It is for frustrated parents who don't know what to do. The name is 'Plain Answers for Families'. The design should, therefore, NOT have hearts and flowers but, instead, look clean and direct. My logo has shades of blue so that would be nice. I have done this work for over 30 years and am well-degreed so would like the design to look stable/established. I have attached my company's logo.

Target Market(s)

Frustrated parents of children - age birth to 20

Industry/Entity Type

Coaching/Counseling for parents

Font styles to use
Serif
Sans Serif

Colors
0054AA
0677BA
7BADD7
CADEEF
E8F1F8

Requirements
Must have
• A look that is clean/bold/direct and professional. Serious.
Nice to have
• If it looks good, my name with my degrees behind my name. MS, MEd. Another thought would be to have a background image of a frustrated parent. Not sure if that would be good or look too busy.
Should not have
• Flowers, fluff, soft appearance, pinks, light colors

```html
<!DOCTYPE html>
<html lang="en">
<head>
<meta charset="utf-8">
<title>Plain Answers for Families – Podcast Cover</title>
<link href="https://fonts.googleapis.com/css2?family=Cinzel:wght@700&family=Montserrat:wght@200;800&display=swap" rel="stylesheet">
<style>
  :root {
    --blue-deep: #0054AA;
    --blue-field: #0A66B1;
    --blue-mid: #0677BA;
    --blue-line: #1490DC;
    --blue-soft: #7BADD7;
    --blue-pale: #CADEEF;
    --white: #FFFFFF;
  }
  html, body {
    margin: 0;
    width: 1200px;
    height: 1200px;
    overflow: hidden;
    background: var(--white);
  }
  .cover {
    display: block;
    width: 1200px;
    height: 1200px;
  }
  .cover__title {
    font-family: "Cinzel", "Times New Roman", serif;
    font-weight: 700;
    font-size: 118px;
    fill: var(--white);
  }
  .cover__host-lead {
    font-family: "Montserrat", Arial, sans-serif;
    font-weight: 200;
    font-size: 80px;
    fill: var(--white);
  }
  .cover__host-name {
    font-family: "Montserrat", Arial, sans-serif;
    font-weight: 800;
    font-size: 80px;
    fill: var(--white);
  }
  .cover__degrees {
    font-family: "Montserrat", Arial, sans-serif;
    font-weight: 800;
    font-size: 128px;
  }
  .cover__brand {
    font-family: "Cinzel", "Times New Roman", serif;
    font-weight: 700;
    font-size: 54px;
    fill: var(--blue-deep);
  }
  .cover__brand--sub {
    font-size: 38px;
  }
  .cover__rule {
    stroke: var(--blue-line);
    stroke-width: 26;
  }
</style>
</head>
<body>
<svg class="cover" viewBox="60 60 1380 1380" xmlns="http://www.w3.org/2000/svg">
  <defs>
    <radialGradient id="field-glow" cx="0.45" cy="0.4" r="0.8">
      <stop offset="0" stop-color="#0B6CB8"/>
      <stop offset="1" stop-color="#0A5FA6"/>
    </radialGradient>
    <linearGradient id="conversation-tone" x1="0" y1="0" x2="1" y2="1">
      <stop offset="0" stop-color="#1382CC"/>
      <stop offset="1" stop-color="#0E74C0"/>
    </linearGradient>
    <linearGradient id="degree-fade" x1="0" y1="0" x2="0" y2="1">
      <stop offset="0" stop-color="var(--blue-soft)"/>
      <stop offset="1" stop-color="var(--blue-pale)" stop-opacity="0.55"/>
    </linearGradient>
  </defs>

  <!-- blue field -->
  <rect class="cover__field" x="60" y="60" width="1380" height="1380" fill="url(#field-glow)"/>

  <!-- show title -->
  <text class="cover__title" x="118" y="330">PLAIN ANSWERS</text>
  <text class="cover__title" x="118" y="485">FOR FAMILIES</text>

  <!-- conversation line with central graphic area -->
  <line class="cover__rule" x1="60" y1="757" x2="396" y2="757"/>
  <line class="cover__rule" x1="1114" y1="757" x2="1440" y2="757"/>
  <rect class="cover__conversation" x="396" y="597" width="718" height="300" fill="url(#conversation-tone)"
        role="img" aria-label="Two outlined speech bubbles facing each other in conversation"/>

  <!-- host -->
  <text x="1380" y="1060" text-anchor="end"><tspan class="cover__host-lead">WITH </tspan><tspan class="cover__host-name">DANA MERROW</tspan></text>
  <text class="cover__degrees" x="1380" y="1180" text-anchor="end" fill="url(#degree-fade)">MS. MEd</text>

  <!-- lower bands -->
  <polygon class="cover__stripe" points="690,1215 735,1215 530,1440 485,1440" fill="var(--blue-mid)"/>
  <polygon class="cover__band" points="60,1308 512,1308 407,1440 60,1440" fill="var(--white)"/>
  <polygon class="cover__band" points="750,1185 1440,1185 1440,1440 525,1440" fill="var(--white)"/>

  <!-- company name -->
  <circle class="cover__brand-mark" cx="1050" cy="1262" r="46" fill="var(--blue-mid)"/>
  <text class="cover__brand" x="1050" y="1368" text-anchor="middle">BRIGHTPATH</text>
  <text class="cover__brand cover__brand--sub" x="1050" y="1418" text-anchor="middle">PARENTING</text>
</svg>
</body>
</html>
```